Structural Engineering Firm Looking for High-Impact Lead Generation Focused Design (for B2B)

A well-established structural engineering firm in the UK wants a new website designed for them which will help them realise more business from online. Directly through the website as well as Ads and lead platforms. They need to compare favourably to competitors and have clarity. Current Site is here: http://www.marlowgrantpartners.example/ - you can take imagery from this site if you want to help with the design.
Updates

Target Market(s)

Homeowners, Architects, Designers, Construction Companies and Landlords

Industry/Entity Type

Professional Services

Number of Pages Required

5+ page

Font styles to use
Sans Serif

Requirements
Must have
• A Strong, Simple and Professional Design with a Focus on Lead Generation
Nice to have
• Creativity in the Detail, Clear Messaging
Should not have
• Too Much Colour, Too 'Consumer', Too Much Variation

```html
<!DOCTYPE html>
<html lang="en">
<head>
<meta charset="utf-8">
<title>Marlow Grant Partners – Structural Engineering &amp; Party Wall Surveying</title>
<link href="https://fonts.googleapis.com/css2?family=Oswald:wght@500&family=Roboto:wght@400;500;700&display=swap" rel="stylesheet">
<style>
:root{
  --red:#c3323b;
  --purple:#3b2f45;
  --ink:#3a3a3a;
  --muted:#7a7a7a;
  --light:#f1f1f1;
  --black:#1b1b1b;
  --white:#ffffff;
}
*{box-sizing:border-box;margin:0;padding:0}
html,body{width:1200px;height:5008px;overflow:hidden}
body{position:relative;background:var(--white);font-family:'Roboto',Arial,sans-serif;color:var(--ink)}
.abs{position:absolute}
.heading{font-family:'Oswald','Arial Narrow',sans-serif;font-weight:500;text-transform:uppercase;color:var(--ink);letter-spacing:.3px}
.body-copy{font-size:13.5px;line-height:26px;color:var(--muted);text-align:justify}
.body-copy p+p{margin-top:12px}
.photo{border:8px solid var(--white);border-radius:16px;box-shadow:0 3px 14px rgba(0,0,0,.18);overflow:hidden}
.photo div{width:100%;height:100%;border-radius:9px}

/* top bar & header */
.utility-bar{left:716px;top:0;width:484px;height:40px;background:var(--purple);border-bottom-left-radius:30px;display:flex;align-items:center;justify-content:flex-end;padding-right:78px;gap:12px;color:#fff;font-size:13.5px}
.utility-bar span.sep{opacity:.7}
.logo{left:111px;top:24px;font-family:'Roboto',sans-serif;font-weight:500;font-size:27px;line-height:29px;color:var(--ink);text-transform:uppercase;letter-spacing:-.5px}
.main-nav{top:72px;left:384px;display:flex;gap:26px;font-size:13.5px;font-weight:700;color:#222}
.main-nav .active{color:var(--red)}

/* hero */
.hero{left:0;top:113px;width:1200px;height:601px;background:linear-gradient(180deg,#1f2a22 0%,#394337 35%,#6b5a44 62%,#8a6a4a 78%,#4f6a33 100%)}
.hero-title{left:111px;top:336px;font-size:34px;line-height:51px;color:#fff}
.hero-arrow{top:395px;width:36px;height:36px}
.quote-band{left:111px;top:626px;width:976px;height:171px;background:var(--red);border-radius:86px}
.quote-text{left:189px;top:672px;font-size:26px;line-height:43px;color:#fff}
.select{height:52px;background:#fff;border-radius:26px;display:flex;align-items:center;justify-content:space-between;padding:0 22px;font-size:14px;font-weight:500;color:#222;box-shadow:0 2px 8px rgba(0,0,0,.15)}

/* process */
.band-grey{left:0;width:1200px;background:var(--light)}
.step{width:221px;height:276px;background:#fff;border-radius:10px;box-shadow:0 2px 10px rgba(0,0,0,.15);padding:7px}
.step .img{width:100%;height:238px;border-radius:6px}
.step .label{position:absolute;left:15px;right:15px;bottom:-12px;height:48px;background:#fff;border-radius:8px;box-shadow:0 2px 8px rgba(0,0,0,.15);display:flex;align-items:center;justify-content:center;font-size:17px;font-weight:700;color:var(--red);text-transform:uppercase}

/* partnership */
.partnership{left:0;top:2312px;width:1200px;height:374px;background:linear-gradient(135deg,#43364d,#2f2538)}
.btn{height:50px;border-radius:25px;display:flex;align-items:center;justify-content:center;font-size:13px;font-weight:700;text-transform:uppercase}

/* news */
.news-card{width:310px;height:393px;background:#fff;border-radius:10px;box-shadow:0 2px 10px rgba(0,0,0,.12);padding:8px}
.news-card .img{height:190px;border-radius:6px}
.news-card .meta{margin:26px 0 0 10px;font-size:13.5px;color:var(--ink);display:flex;align-items:center;gap:10px}
.news-card h3{margin:18px 10px 0;font-size:15.5px;font-weight:500;text-transform:uppercase}
.news-card p{margin:14px 10px 0;font-size:13px;line-height:22px;color:var(--muted);text-align:justify}
.news-card .more{margin:16px 10px 0;font-size:13px;font-weight:700;color:var(--red);display:flex;align-items:center;gap:8px}

/* contact */
.office{width:474px;height:482px;border-radius:14px;padding:8px;color:#fff;box-shadow:0 3px 12px rgba(0,0,0,.2)}
.office .map{height:273px;border-radius:8px}
.office h3{margin:36px 0 0 26px;font-size:19px;font-weight:500;text-transform:uppercase}
.office ul{list-style:none;margin:20px 0 0 26px;font-size:14px;line-height:26px}
.office li{display:flex;gap:18px}
.office li+li{margin-top:10px}

/* footer */
.footer{left:0;top:4582px;width:1200px;height:426px;background:var(--black);color:#fff}
.footer-col{top:63px}
.footer-col h4{font-size:15.5px;font-weight:700;text-transform:uppercase;margin-bottom:16px}
.footer-col ul{list-style:none;font-size:13px;line-height:27px}
.footer-col li{display:flex;align-items:center;gap:16px}
.contact-strip{left:111px;top:306px;width:976px;height:50px;border-radius:25px;background:var(--red);display:flex;align-items:center;font-size:12.5px}
.strip-item{position:absolute;display:flex;align-items:center;gap:18px}
.strip-item .circle{width:40px;height:40px;border-radius:50%;background:#fff;display:flex;align-items:center;justify-content:center}
.legal{top:385px;width:1200px;text-align:center;font-size:12px;color:#ddd}
</style>
</head>
<body>

<!-- header -->
<div class="abs utility-bar"><span>Gallery</span><span class="sep">|</span><span>Blog</span><span class="sep">|</span><span>About Us</span><span class="sep">|</span><span>Contact Us</span></div>
<div class="abs logo">Marlow Grant<br>Partners</div>
<nav class="abs main-nav"><span class="active">HOME</span><span>STRUCTURAL DESIGN</span><span>STRUCTURAL SURVEYS</span><span>PLANNING</span><span>PARTY WALL</span><span>PARTNERS</span></nav>

<!-- hero -->
<div class="abs hero" role="img" aria-label="Modern white two-storey house with large glazed walls lit at dusk, trees behind and a lawn in front"></div>
<h1 class="abs heading hero-title">Efficient and professional<br>structural engineering &amp;<br>party wall surveying</h1>
<svg class="abs hero-arrow" style="left:40px" viewBox="0 0 36 36"><circle cx="18" cy="18" r="16" fill="none" stroke="#fff" stroke-width="1.6"/><path d="M21 11l-7 7 7 7" fill="none" stroke="#fff" stroke-width="2"/></svg>
<svg class="abs hero-arrow" style="left:1124px" viewBox="0 0 36 36"><circle cx="18" cy="18" r="16" fill="none" stroke="#fff" stroke-width="1.6"/><path d="M15 11l7 7-7 7" fill="none" stroke="#fff" stroke-width="2"/></svg>
<div class="abs quote-band"></div>
<div class="abs heading quote-text" style="color:#fff">Get a competitive quote from<br>the local experts</div>
<div class="abs select" style="left:599px;top:687px;width:411px"><span>What service are you looking for?</span><svg width="12" height="8" viewBox="0 0 12 8"><path d="M1 1l5 5 5-5" fill="none" stroke="#222" stroke-width="1.8"/></svg></div>

<!-- structural engineers -->
<div class="abs photo" style="left:111px;top:889px;width:486px;height:369px"><div role="img" aria-label="Tall brick townhouse with a modern rear extension and landscaped garden" style="background:linear-gradient(180deg,#b8c9d8 0%,#8c7a66 40%,#6d5a47 65%,#6e8a4c 100%)"></div></div>
<h2 class="abs heading" style="left:653px;top:924px;font-size:29px;line-height:39px">Structural engineers in<br>London and the south east</h2>
<div class="abs body-copy" style="left:653px;top:1024px;width:436px">
<p>Sed ut perspiciatis unde omnis iste natus error sit voluptatem accusantium doloremque laudantium, totam rem aperiam, eaque ipsa quae ab illo inventore veritatis et quasi architecto beatae vitae dicta sunt explicabo voluptatem quiea.</p>
<p>At vero eos et accusamus et iusto odio dignissimos ducimus qui blanditiis praesentium voluptatum deleniti atque corrupti quos dolores et quas molestias excepturiea.</p>
</div>

<!-- party wall -->
<h2 class="abs heading" style="left:111px;top:1354px;font-size:29px;line-height:39px">Choose the party wall<br>specialists</h2>
<div class="abs body-copy" style="left:111px;top:1454px;width:436px">
<p>Sed ut perspiciatis unde omnis iste natus error sit voluptatem accusantium doloremque laudantium, totam rem aperiam, eaque ipsa quae ab illo inventore veritatis et quasi architecto beatae vitae dicta sunt explicabo voluptatem quiea.</p>
<p>At vero eos et accusamus et iusto odio dignissimos ducimus qui blanditiis praesentium voluptatum deleniti atque corrupti quos dolores et quas molestias excepturiea.</p>
</div>
<div class="abs photo" style="left:601px;top:1320px;width:486px;height:366px"><div role="img" aria-label="Rear extension with framed glass doors, dark brick plinth and garden planting" style="background:linear-gradient(180deg,#d8cfc2 0%,#a9a79a 45%,#4f5a4a 70%,#3a3a3e 100%)"></div></div>

<!-- process -->
<div class="abs band-grey" style="top:1783px;height:528px"></div>
<h2 class="abs heading" style="left:0;top:1844px;width:1200px;text-align:center;font-size:27px;line-height:39px">From drawing to delivered we support<br>you every step to the way</h2>
<div class="abs step" style="left:111px;top:1964px"><div class="img" role="img" aria-label="White floating staircase in a bright interior" style="background:linear-gradient(135deg,#e8e8e8,#8a8a8a 60%,#3a3a3a)"></div><div class="label">Brief</div></div>
<div class="abs step" style="left:364px;top:1964px"><div class="img" role="img" aria-label="Open-plan kitchen and dining room with yellow chairs" style="background:linear-gradient(180deg,#d9d2c4,#a88f6a 55%,#c9a84a)"></div><div class="label">Design</div></div>
<div class="abs step" style="left:615px;top:1964px"><div class="img" role="img" aria-label="Window seat with a wide picture window over the city" style="background:linear-gradient(180deg,#f2f2f2,#c6cdd2 50%,#9a8a6e)"></div><div class="label">Refine</div></div>
<div class="abs step" style="left:866px;top:1964px"><div class="img" role="img" aria-label="Brick rear extension with black framed glazing" style="background:linear-gradient(180deg,#cfd4d8,#6e5a4c 50%,#3c3430)"></div><div class="label">Deliver</div></div>

<!-- partnership -->
<div class="abs partnership"></div>
<h2 class="abs heading" style="left:0;top:2372px;width:1200px;text-align:center;font-size:29px;color:#fff">We work in partnership</h2>
<p class="abs" style="left:130px;top:2439px;width:940px;text-align:center;font-size:13.5px;line-height:26px;color:#fff">At vero eos et accusamus et iusto odio dignissimos ducimus qui blanditiis praesentium voluptatum deleniti atque corrupti quos dolores et quas molestias excepturi sint occaecati cupiditate non provident, similique sunt in culpa qui officia deserunt mollitia animi, id est laborum et dolorum fuga. Et harum quidem rerum facilis est et expedita distinctio. Nam libero tempore, cum soluta nobis est eligendi optio cumque nihil impedit quo minus id quod maxime placeat facere possimus id quod maxime facere possimus, omnis voluptasea.</p>
<div class="abs btn" style="left:350px;top:2567px;width:241px;background:var(--red);color:#fff">Partner with us</div>
<div class="abs btn" style="left:605px;top:2567px;width:245px;background:#fff;color:var(--red)">Introduce us to your team</div>

<!-- fast turnaround -->
<div class="abs photo" style="left:111px;top:2781px;width:486px;height:364px"><div role="img" aria-label="Contemporary grey kitchen with wooden worktop, gas hob and brick wall" style="background:linear-gradient(135deg,#cfcfcf,#6f7072 50%,#b08a5a 80%,#55575a)"></div></div>
<h2 class="abs heading" style="left:653px;top:2813px;font-size:29px">Need a fast turnaround?</h2>
<div class="abs select" style="left:653px;top:2873px;width:413px"><span>What service are you looking for?</span><svg width="12" height="8" viewBox="0 0 12 8"><path d="M1 1l5 5 5-5" fill="none" stroke="#222" stroke-width="1.8"/></svg></div>
<div class="abs body-copy" style="left:653px;top:2953px;width:436px"><p>Sed ut perspiciatis unde omnis iste natus error sit voluptatem accusantium doloremque laudantium, totam rem aperiam, eaque ipsa quae ab illo inventore veritatis et quasi architecto beatae vitae dicta sunt explicabo voluptatem quiea. At vero eos et accusamus et iusto odio dignissimos ducimus qui blanditiis praesentium voluptat um deleniti atque corrupti quos doloresea.</p></div>

<!-- news -->
<div class="abs band-grey" style="top:3248px;height:599px"></div>
<h2 class="abs heading" style="left:0;top:3311px;width:1200px;text-align:center;font-size:31px">Latest news</h2>
<article class="abs news-card" style="left:111px;top:3386px">
  <div class="img" role="img" aria-label="Large red-brick country house with timber deck" style="background:linear-gradient(180deg,#9fb6cf,#8a4a36 55%,#c9b08a)"></div>
  <div class="meta"><svg width="14" height="14" viewBox="0 0 14 14"><rect x="1" y="2" width="12" height="11" rx="1.5" fill="var(--red)"/><rect x="3" y="6" width="8" height="5" fill="#fff"/></svg>12 Apr 2021</div>
  <h3>At vero eos et accusamus</h3>
  <p>Sed ut perspiciatis unde omnis iste natus error sit voluptatem accusantium doloremque laudantium, totam rem aper.</p>
  <div class="more">Read more <svg width="13" height="13" viewBox="0 0 13 13"><circle cx="6.5" cy="6.5" r="6.5" fill="var(--red)"/><path d="M5 3.5l3 3-3 3" fill="none" stroke="#fff" stroke-width="1.6"/></svg></div>
</article>
<article class="abs news-card" style="left:445px;top:3386px">
  <div class="img" role="img" aria-label="Modern house with white render, brick wing and red garage door" style="background:linear-gradient(180deg,#d6dde2,#7a6e62 50%,#b23a34 75%,#5a6a48)"></div>
  <div class="meta"><svg width="14" height="14" viewBox="0 0 14 14"><rect x="1" y="2" width="12" height="11" rx="1.5" fill="var(--red)"/><rect x="3" y="6" width="8" height="5" fill="#fff"/></svg>12 Apr 2021</div>
  <h3>At vero eos et accusamus</h3>
  <p>Sed ut perspiciatis unde omnis iste natus error sit voluptatem accusantium doloremque laudantium, totam rem aper.</p>
  <div class="more">Read more <svg width="13" height="13" viewBox="0 0 13 13"><circle cx="6.5" cy="6.5" r="6.5" fill="var(--red)"/><path d="M5 3.5l3 3-3 3" fill="none" stroke="#fff" stroke-width="1.6"/></svg></div>
</article>
<article class="abs news-card" style="left:780px;top:3386px">
  <div class="img" role="img" aria-label="Living room with white sofa and black steel glazed partition" style="background:linear-gradient(135deg,#eeeeee,#b9b6b0 50%,#3c3c3c)"></div>
  <div class="meta"><svg width="14" height="14" viewBox="0 0 14 14"><rect x="1" y="2" width="12" height="11" rx="1.5" fill="var(--red)"/><rect x="3" y="6" width="8" height="5" fill="#fff"/></svg>12 Apr 2021</div>
  <h3>At vero eos et accusamus</h3>
  <p>Sed ut perspiciatis unde omnis iste natus error sit voluptatem accusantium doloremque laudantium, totam rem aper.</p>
  <div class="more">Read more <svg width="13" height="13" viewBox="0 0 13 13"><circle cx="6.5" cy="6.5" r="6.5" fill="var(--red)"/><path d="M5 3.5l3 3-3 3" fill="none" stroke="#fff" stroke-width="1.6"/></svg></div>
</article>

<!-- contact -->
<h2 class="abs heading" style="left:0;top:3922px;width:1200px;text-align:center;font-size:31px">Contact us</h2>
<section class="abs office" style="left:111px;top:4005px;background:var(--red)">
  <div class="map" role="img" aria-label="Street map of the London office area" style="background:linear-gradient(135deg,#eef0f2,#dde3e8 60%,#e9ecd8)"></div>
  <h3>Marlow Grant Partners London</h3>
  <ul>
    <li><svg width="12" height="16" viewBox="0 0 12 16" style="margin-top:5px;flex:none"><path d="M6 0a6 6 0 016 6c0 4.5-6 10-6 10S0 10.5 0 6a6 6 0 016-6z" fill="#fff"/><circle cx="6" cy="6" r="2.2" fill="var(--red)"/></svg><span>Unit 4 Kelby Yard,<br>22 Ashcombe Road, London SW9 1AA<br>United Kingdom</span></li>
    <li><svg width="14" height="14" viewBox="0 0 14 14" style="margin-top:6px;flex:none"><path d="M3 0l3 3-1.5 2a8 8 0 004.5 4.5L11 8l3 3-2 3C6 14 0 8 0 2z" fill="#fff"/></svg><span>+44 (0) 20 7946 0123</span></li>
  </ul>
</section>
<section class="abs office" style="left:613px;top:4005px;background:var(--purple)">
  <div class="map" role="img" aria-label="Road map of the Sussex office area with surrounding villages" style="background:linear-gradient(180deg,#e8edf1 0%,#e4e8ec 50%,#d9e7c9 65%,#cfe2bd 100%)"></div>
  <h3>Marlow Grant Partners Sussex</h3>
  <ul>
    <li><svg width="12" height="16" viewBox="0 0 12 16" style="margin-top:5px;flex:none"><path d="M6 0a6 6 0 016 6c0 4.5-6 10-6 10S0 10.5 0 6a6 6 0 016-6z" fill="#fff"/><circle cx="6" cy="6" r="2.2" fill="var(--purple)"/></svg><span>Hollin Barn<br>Weald Lane<br>Ashbourne, BN99 2ZZ</span></li>
    <li><svg width="14" height="14" viewBox="0 0 14 14" style="margin-top:6px;flex:none"><path d="M3 0l3 3-1.5 2a8 8 0 004.5 4.5L11 8l3 3-2 3C6 14 0 8 0 2z" fill="#fff"/></svg><span>+44 (0) 1632 960 517</span></li>
  </ul>
</section>

<!-- footer -->
<footer class="abs footer">
  <div class="abs footer-col" style="left:140px"><h4>Design</h4><ul>
    <li><svg width="11" height="11" viewBox="0 0 11 11"><circle cx="5.5" cy="5.5" r="5.5" fill="var(--red)"/><path d="M4.3 3l2.5 2.5-2.5 2.5" fill="none" stroke="#1b1b1b" stroke-width="1.4"/></svg>Design Advice</li>
    <li><svg width="11" height="11" viewBox="0 0 11 11"><circle cx="5.5" cy="5.5" r="5.5" fill="var(--red)"/><path d="M4.3 3l2.5 2.5-2.5 2.5" fill="none" stroke="#1b1b1b" stroke-width="1.4"/></svg>Lofts</li>
    <li><svg width="11" height="11" viewBox="0 0 11 11"><circle cx="5.5" cy="5.5" r="5.5" fill="var(--red)"/><path d="M4.3 3l2.5 2.5-2.5 2.5" fill="none" stroke="#1b1b1b" stroke-width="1.4"/></svg>Side Returns</li>
    <li><svg width="11" height="11" viewBox="0 0 11 11"><circle cx="5.5" cy="5.5" r="5.5" fill="var(--red)"/><path d="M4.3 3l2.5 2.5-2.5 2.5" fill="none" stroke="#1b1b1b" stroke-width="1.4"/></svg>Basements</li>
    <li><svg width="11" height="11" viewBox="0 0 11 11"><circle cx="5.5" cy="5.5" r="5.5" fill="var(--red)"/><path d="M4.3 3l2.5 2.5-2.5 2.5" fill="none" stroke="#1b1b1b" stroke-width="1.4"/></svg>House Conversion</li>
    <li><svg width="11" height="11" viewBox="0 0 11 11"><circle cx="5.5" cy="5.5" r="5.5" fill="var(--red)"/><path d="M4.3 3l2.5 2.5-2.5 2.5" fill="none" stroke="#1b1b1b" stroke-width="1.4"/></svg>Temporary Works</li>
    <li><svg width="11" height="11" viewBox="0 0 11 11"><circle cx="5.5" cy="5.5" r="5.5" fill="var(--red)"/><path d="M4.3 3l2.5 2.5-2.5 2.5" fill="none" stroke="#1b1b1b" stroke-width="1.4"/></svg>Surveys</li>
  </ul></div>
  <div class="abs footer-col" style="left:391px"><h4>Quick links</h4><ul>
    <li><svg width="11" height="11" viewBox="0 0 11 11"><circle cx="5.5" cy="5.5" r="5.5" fill="var(--red)"/><path d="M4.3 3l2.5 2.5-2.5 2.5" fill="none" stroke="#1b1b1b" stroke-width="1.4"/></svg>Partners</li>
    <li><svg width="11" height="11" viewBox="0 0 11 11"><circle cx="5.5" cy="5.5" r="5.5" fill="var(--red)"/><path d="M4.3 3l2.5 2.5-2.5 2.5" fill="none" stroke="#1b1b1b" stroke-width="1.4"/></svg>Home</li>
    <li><svg width="11" height="11" viewBox="0 0 11 11"><circle cx="5.5" cy="5.5" r="5.5" fill="var(--red)"/><path d="M4.3 3l2.5 2.5-2.5 2.5" fill="none" stroke="#1b1b1b" stroke-width="1.4"/></svg>Gallery</li>
    <li><svg width="11" height="11" viewBox="0 0 11 11"><circle cx="5.5" cy="5.5" r="5.5" fill="var(--red)"/><path d="M4.3 3l2.5 2.5-2.5 2.5" fill="none" stroke="#1b1b1b" stroke-width="1.4"/></svg>Blog</li>
    <li><svg width="11" height="11" viewBox="0 0 11 11"><circle cx="5.5" cy="5.5" r="5.5" fill="var(--red)"/><path d="M4.3 3l2.5 2.5-2.5 2.5" fill="none" stroke="#1b1b1b" stroke-width="1.4"/></svg>About</li>
    <li><svg width="11" height="11" viewBox="0 0 11 11"><circle cx="5.5" cy="5.5" r="5.5" fill="var(--red)"/><path d="M4.3 3l2.5 2.5-2.5 2.5" fill="none" stroke="#1b1b1b" stroke-width="1.4"/></svg>Contact Us</li>
  </ul></div>
  <div class="abs footer-col" style="left:603px"><h4>Party wall</h4><ul>
    <li><svg width="11" height="11" viewBox="0 0 11 11"><circle cx="5.5" cy="5.5" r="5.5" fill="var(--red)"/><path d="M4.3 3l2.5 2.5-2.5 2.5" fill="none" stroke="#1b1b1b" stroke-width="1.4"/></svg>Serving Party Wall Notices</li>
    <li><svg width="11" height="11" viewBox="0 0 11 11"><circle cx="5.5" cy="5.5" r="5.5" fill="var(--red)"/><path d="M4.3 3l2.5 2.5-2.5 2.5" fill="none" stroke="#1b1b1b" stroke-width="1.4"/></svg>Forming Party Wall Awards</li>
    <li><svg width="11" height="11" viewBox="0 0 11 11"><circle cx="5.5" cy="5.5" r="5.5" fill="var(--red)"/><path d="M4.3 3l2.5 2.5-2.5 2.5" fill="none" stroke="#1b1b1b" stroke-width="1.4"/></svg>Condition Schedules</li>
    <li><svg width="11" height="11" viewBox="0 0 11 11"><circle cx="5.5" cy="5.5" r="5.5" fill="var(--red)"/><path d="M4.3 3l2.5 2.5-2.5 2.5" fill="none" stroke="#1b1b1b" stroke-width="1.4"/></svg>Minor Residential Works</li>
  </ul></div>
  <div class="abs footer-col" style="left:893px"><h4>Planning</h4><ul>
    <li><svg width="11" height="11" viewBox="0 0 11 11"><circle cx="5.5" cy="5.5" r="5.5" fill="var(--red)"/><path d="M4.3 3l2.5 2.5-2.5 2.5" fill="none" stroke="#1b1b1b" stroke-width="1.4"/></svg>Planning Applications</li>
    <li><svg width="11" height="11" viewBox="0 0 11 11"><circle cx="5.5" cy="5.5" r="5.5" fill="var(--red)"/><path d="M4.3 3l2.5 2.5-2.5 2.5" fill="none" stroke="#1b1b1b" stroke-width="1.4"/></svg>Planning Reports</li>
  </ul></div>
  <svg class="abs" style="left:894px;top:160px" width="120" height="36" viewBox="0 0 120 36" aria-label="Social links">
    <circle cx="18" cy="18" r="17" fill="var(--red)"/><circle cx="59" cy="18" r="17" fill="#fff"/><circle cx="100" cy="18" r="17" fill="#fff"/>
  </svg>
  <div class="abs contact-strip">
    <div class="strip-item" style="left:38px"><span class="circle"><svg width="14" height="14" viewBox="0 0 14 14"><path d="M3 0l3 3-1.5 2a8 8 0 004.5 4.5L11 8l3 3-2 3C6 14 0 8 0 2z" fill="var(--red)"/></svg></span><span><b>LONDON:</b> +44 (0) 20 7946 0123</span></div>
    <div class="strip-item" style="left:330px"><span class="circle"><svg width="14" height="14" viewBox="0 0 14 14"><path d="M3 0l3 3-1.5 2a8 8 0 004.5 4.5L11 8l3 3-2 3C6 14 0 8 0 2z" fill="var(--red)"/></svg></span><span><b>SUSSEX:</b> +44 (0) 1632 960 517</span></div>
    <div class="strip-item" style="left:620px"><span class="circle"><svg width="16" height="12" viewBox="0 0 16 12"><rect width="16" height="12" rx="1.5" fill="var(--red)"/><path d="M1 1l7 5.5L15 1" fill="none" stroke="#fff" stroke-width="1.4"/></svg></span><span><b>EMAIL:</b> info@marlowgrantpartners.example</span></div>
  </div>
  <div class="abs legal">© 2022 MARLOW GRANT PARTNERS LTD &nbsp;|&nbsp; Privacy Policy &nbsp;|&nbsp; Terms Of Use &nbsp;|&nbsp; Site Map &nbsp;|&nbsp; Contact Us</div>
</footer>

</body>
</html>
```